E-Waste Recycling Company Business Card

New Electronic Recycling Company based in Long Island, New York called "Lady Rust-a-bunch" We take outdated computers, components, electrical wire, circuit breakers, ink cartridges, etc. We look mostly for donated items that we recycle for our customers but will pay for large quantities from businesses. The design should reflect that we are environmentally friendly and our unique 7Q Obliteration process that ensures all personal data is wiped clean off hard drives. Please use our attached logo
Industry/Entity Type
Electrical

```html
<!DOCTYPE html>
<html lang="en">
<head>
<meta charset="utf-8">
<title>Lady Rust-a-bunch Business Card</title>
<link href="https://fonts.googleapis.com/css2?family=Open+Sans:wght@400;600;700&display=swap" rel="stylesheet">
<style>
  :root {
    --bg: #ececec;
    --white: #ffffff;
    --green: #46b82c;
    --green-light: #86d62a;
    --green-deep: #2f9a22;
    --green-text: #3aa82a;
    --ink: #222222;
    --ink-soft: #444444;
    --rule: #d9d9d9;
  }
  * { box-sizing: border-box; margin: 0; padding: 0; }
  html, body { width: 1200px; height: 900px; overflow: hidden; }
  body {
    background: var(--bg);
    font-family: "Open Sans", Arial, sans-serif;
    position: relative;
  }
  .card {
    position: absolute;
    top: 100px;
    width: 420px;
    height: 700px;
    border-radius: 30px;
    overflow: hidden;
  }
  .card-front { left: 150px; background: var(--white); }
  .card-back {
    left: 630px;
    background: radial-gradient(circle at 50% 48%, var(--green-light) 0%, #5cc428 45%, var(--green-deep) 100%);
  }

  .brand-name {
    position: absolute;
    left: 0; right: 0;
    text-align: center;
    font-weight: 700;
    font-size: 34px;
    line-height: 1.15;
    color: var(--green-text);
  }
  .card-front .brand-name { top: 110px; }
  .card-back .brand-name { top: 300px; color: var(--white); }

  .divider {
    position: absolute;
    left: 60px; right: 60px;
    top: 290px;
    height: 2px;
    background: linear-gradient(90deg, transparent, var(--rule) 30%, var(--rule) 70%, transparent);
  }

  .person { position: absolute; left: 60px; top: 318px; }
  .person-name { font-size: 27px; font-weight: 700; color: var(--green-text); line-height: 1.2; }
  .person-title { font-size: 17px; color: var(--ink); margin-top: 4px; }

  .address {
    position: absolute; left: 60px; top: 405px;
    font-size: 17px; line-height: 1.3; color: var(--ink);
  }

  .contacts {
    position: absolute; left: 80px; top: 480px;
    list-style: none;
  }
  .contacts li {
    display: flex; align-items: center;
    font-size: 17px; color: var(--ink);
    height: 30px;
  }
  .contacts svg { width: 20px; height: 20px; margin-right: 12px; flex: none; }

  .web-band {
    position: absolute; left: 0; right: 0; top: 612px;
    height: 44px;
    background: var(--green);
    color: var(--white);
    font-weight: 700; font-size: 17px;
    display: flex; align-items: center; justify-content: center;
  }

  .accepts {
    position: absolute; left: 0; right: 0; top: 80px;
    text-align: center; color: #1c5a12;
  }
  .accepts-heading { font-weight: 700; font-size: 17px; color: var(--ink); margin-bottom: 2px; }
  .accepts-list { list-style: none; font-size: 15px; line-height: 1.3; }

  .back-web {
    position: absolute; left: 0; right: 0; bottom: 70px;
    text-align: center;
    color: var(--white); font-weight: 700; font-size: 18px;
  }
</style>
</head>
<body>

  <section class="card card-front">
    <div class="brand-name">Lady<br>Rust-a-bunch</div>
    <div class="divider"></div>

    <div class="person">
      <div class="person-name">Your Name</div>
      <div class="person-title">Title</div>
    </div>

    <div class="address">NMLS#5550100200<br>n 12th street Brookhaven, NY 11719</div>

    <ul class="contacts">
      <li>
        <svg viewBox="0 0 20 20" aria-hidden="true"><circle cx="10" cy="10" r="10" fill="var(--green)"/><path d="M6.5 5.5c.6-.5 1.3-.3 1.6.3l.8 1.5c.2.5 0 1-.4 1.3l-.5.4c.5 1.2 1.5 2.2 2.7 2.7l.4-.5c.3-.4.8-.6 1.3-.4l1.5.8c.6.3.8 1 .3 1.6-.9 1-2.3 1.1-3.6.4-1.9-1-3.4-2.5-4.4-4.4-.7-1.3-.6-2.7.3-3.7z" fill="#fff"/></svg>
        555.010.2841
      </li>
      <li>
        <svg viewBox="0 0 20 20" aria-hidden="true"><circle cx="10" cy="10" r="10" fill="var(--green)"/><rect x="7" y="4.5" width="6" height="11" rx="1.2" fill="#fff"/><rect x="8" y="6" width="4" height="6.5" fill="var(--green)"/></svg>
        555.010.6637
      </li>
      <li>
        <svg viewBox="0 0 20 20" aria-hidden="true"><circle cx="10" cy="10" r="10" fill="var(--green)"/><rect x="7" y="5" width="6" height="4" fill="#fff"/><rect x="5" y="8.5" width="10" height="5" rx="1" fill="#fff"/><rect x="7" y="12" width="6" height="3" fill="#fff" stroke="var(--green)" stroke-width=".6"/></svg>
        555.010.4172
      </li>
      <li>
        <svg viewBox="0 0 20 20" aria-hidden="true"><circle cx="10" cy="10" r="10" fill="var(--green)"/><rect x="5" y="6.5" width="10" height="7" rx="1" fill="#fff"/><path d="M5.5 7l4.5 3.5L14.5 7" fill="none" stroke="var(--green)" stroke-width="1"/></svg>
        info@ladyrustabunchrecycling.com
      </li>
    </ul>

    <div class="web-band">www.ladyrustabunchrecycling.com</div>
  </section>

  <section class="card card-back">
    <div class="accepts">
      <div class="accepts-heading">WE TAKE</div>
      <ul class="accepts-list">
        <li>outdated computers</li>
        <li>components</li>
        <li>electrical wire</li>
        <li>circuit breakers</li>
        <li>ink cartridges, etc</li>
      </ul>
    </div>

    <div class="brand-name">Lady<br>Rust-a-bunch</div>

    <div class="back-web">www.ladyrustabunch.com</div>
  </section>

</body>
</html>
```